Larkfield Advisory Group LLC Business Card Design

I'm looking for a fresh, sharp, clean and current/modern format for my company. This is a start up in the professional services (security/risk management consulting) industry. Catering to C-suite executives as well as senior director types of halcyon 800 companies.

Target Market(s)

Halcyon 800 companies and their C-suite staff with particular focus on VP of Human Resources and Director of Security.

Industry/Entity Type

Business

Font styles to use
Serif

Colors
0455a3
9bcb3c
acd037
3377b5
eaf1f7

Requirements
Must have
• Fresh, sharp, clean and current/modern look and feel.

```html
<!DOCTYPE html>
<html lang="en">
<head>
<meta charset="utf-8">
<title>Larkfield Advisory Group — Business Cards</title>
<link href="https://fonts.googleapis.com/css2?family=Montserrat:wght@800&family=Open+Sans:wght@400;600&display=swap" rel="stylesheet">
<style>
  :root{
    --navy:#1f3f86;
    --band:#2e3a8c;
    --band-line:#5f6fc0;
    --green:#6fae2e;
    --ink:#3a3a3a;
    --paper:#ffffff;
    --backdrop:#e7e9ec;
    --rule:#d5d8dd;
  }
  *{box-sizing:border-box;margin:0;padding:0}
  html,body{width:1200px;height:951px;overflow:hidden;background:var(--backdrop)}
  .canvas{position:relative;width:1200px;height:951px}
  .card{position:absolute;width:640px;height:366px;background:var(--paper);border-radius:22px;overflow:hidden;box-shadow:0 10px 28px rgba(0,0,0,.18)}
  .card-front{left:90px;top:70px}
  .card-back{left:470px;top:520px}

  .brand{display:flex;align-items:center;gap:16px}
  .brand-dot{border-radius:50%;background:var(--navy);flex:none}
  .brand-name{font-family:"Montserrat",sans-serif;font-weight:800;color:var(--navy);letter-spacing:.5px;line-height:1.05;text-transform:uppercase}

  .card-front .brand{position:absolute;left:70px;top:100px}
  .card-front .brand-dot{width:88px;height:88px}
  .card-front .brand-name{font-size:34px}
  .card-front .website{position:absolute;left:0;right:0;top:262px;text-align:center;font-family:"Open Sans",sans-serif;font-weight:600;font-size:19px;letter-spacing:1.5px;color:#222}

  .card-back .brand{position:absolute;left:36px;top:96px;gap:10px}
  .card-back .brand-dot{width:48px;height:48px}
  .card-back .brand-name{font-size:19px}
  .divider{position:absolute;left:316px;top:60px;width:1px;height:180px;background:var(--rule)}
  .contact{position:absolute;left:336px;top:66px;font-family:"Open Sans",sans-serif;color:var(--ink)}
  .person-name{font-size:17px;font-weight:600;color:#333}
  .person-title{font-size:14px;color:var(--green);margin-top:2px}
  .lines{list-style:none;margin-top:18px}
  .lines li{display:flex;align-items:flex-start;gap:10px;font-size:14px;line-height:1.4;margin-bottom:6px}
  .lines svg{flex:none;margin-top:3px}
  .band{position:absolute;left:0;right:0;bottom:0;height:78px;background:var(--band);border-top:4px solid var(--band-line)}
  .band .website{display:block;text-align:center;line-height:74px;font-family:"Open Sans",sans-serif;font-size:19px;letter-spacing:1.5px;color:#fff}
</style>
</head>
<body>
<main class="canvas">
  <section class="card card-front" aria-label="Business card front">
    <div class="brand">
      <span class="brand-dot"></span>
      <span class="brand-name">Larkfield<br>Advisory Group</span>
    </div>
    <p class="website">www.larkfieldadvisory.com</p>
  </section>

  <section class="card card-back" aria-label="Business card back">
    <div class="brand">
      <span class="brand-dot"></span>
      <span class="brand-name">Larkfield<br>Advisory Group</span>
    </div>
    <div class="divider"></div>
    <div class="contact">
      <p class="person-name">Marcus Ellery</p>
      <p class="person-title">director</p>
      <ul class="lines">
        <li>
          <svg width="14" height="14" viewBox="0 0 14 14" aria-hidden="true"><path d="M7 1 1 6.5h2V13h3V9h2v4h3V6.5h2z" fill="#6fae2e"/></svg>
          <span>4100 Alder Crest Rd<br>Marlow, TX 78014</span>
        </li>
        <li>
          <svg width="14" height="14" viewBox="0 0 14 14" aria-hidden="true"><circle cx="7" cy="7" r="6" fill="none" stroke="#6fae2e" stroke-width="1.5"/><path d="M4.5 4h1.5l.7 1.6-.9.7a4 4 0 0 0 1.9 1.9l.7-.9 1.6.7v1.5c-3 .3-5.8-2.5-5.5-5.5z" fill="#6fae2e"/></svg>
          <span>512-555-0148</span>
        </li>
        <li>
          <svg width="14" height="14" viewBox="0 0 14 14" aria-hidden="true"><rect x="3.5" y="1" width="7" height="12" rx="1.5" fill="#6fae2e"/><rect x="5" y="3" width="4" height="6" fill="#fff"/></svg>
          <span>512-555-0149</span>
        </li>
        <li>
          <svg width="14" height="14" viewBox="0 0 14 14" aria-hidden="true"><rect x="1" y="3" width="12" height="8" rx="1" fill="#6fae2e"/><path d="M1.5 3.5 7 8l5.5-4.5" fill="none" stroke="#fff" stroke-width="1.2"/></svg>
          <span>info@larkfieldadvisory.com</span>
        </li>
      </ul>
    </div>
    <div class="band"><span class="website">www.larkfieldadvisory.com</span></div>
  </section>
</main>
</body>
</html>
```